New Business Card Design Project

Want a simple but attention grabbing business card. Back Side having mainly our logo and basic info-the front side a typical business card.

Contact Information for Business Card

Hearth & Tile Interiors
218 NW Larkspur Rd. Suite 207
Ankeny, Iowa 50021

phone- 515.482.7093

website is -htidesigns.com

```html
<!DOCTYPE html>
<html lang="en">
<head>
<meta charset="utf-8">
<title>Hearth &amp; Tile Interiors — Business Card</title>
<link rel="stylesheet" href="https://fonts.googleapis.com/css2?family=Lexend:wght@400;500;600&display=swap">
<style>
  :root {
    --navy: #171e2e;
    --ink: #1b2233;
    --muted: #5a5f69;
    --paper: #ffffff;
    --backdrop: #eeeae4;
    --shadow: rgba(30, 30, 40, 0.14);
  }
  * { box-sizing: border-box; margin: 0; padding: 0; }
  html, body {
    width: 1200px;
    height: 1200px;
    overflow: hidden;
  }
  body {
    background: var(--backdrop);
    font-family: "Lexend", sans-serif;
    display: flex;
    flex-direction: column;
    align-items: center;
    justify-content: center;
    gap: 40px;
  }
  .card {
    position: relative;
    width: 760px;
    height: 440px;
    border-radius: 64px;
    box-shadow: 0 10px 28px var(--shadow);
  }
  .card--front {
    background: var(--paper);
    color: var(--ink);
  }
  .card--back {
    background: var(--navy);
    color: var(--paper);
  }

  /* Front side */
  .holder {
    position: absolute;
    left: 58px;
    top: 192px;
  }
  .holder__name {
    font-size: 24px;
    font-weight: 600;
    letter-spacing: 0.06em;
  }
  .holder__role {
    margin-top: 6px;
    font-size: 17px;
    font-weight: 500;
    letter-spacing: 0.08em;
    color: var(--muted);
  }
  .contact {
    position: absolute;
    left: 58px;
    top: 302px;
    list-style: none;
  }
  .contact__item {
    display: flex;
    align-items: center;
    gap: 12px;
    font-size: 18px;
    font-weight: 400;
    letter-spacing: 0.02em;
    height: 30px;
  }
  .contact__icon {
    width: 16px;
    height: 16px;
    flex: none;
  }

  /* Wordmark */
  .wordmark {
    display: flex;
    flex-direction: column;
    align-items: center;
    font-weight: 600;
  }
  .wordmark__mark {
    width: 20px;
    height: 20px;
    background: currentColor;
    margin-bottom: 14px;
  }
  .wordmark__name {
    font-size: 28px;
    letter-spacing: 0.02em;
    text-transform: uppercase;
    line-height: 1;
  }
  .wordmark__sub {
    margin-top: 8px;
    font-size: 11px;
    letter-spacing: 0.75em;
    text-transform: uppercase;
    padding-left: 0.75em;
  }
  .card--front .wordmark {
    position: absolute;
    left: 432px;
    width: 280px;
    top: 162px;
  }
  .card--back .wordmark {
    position: absolute;
    left: 0;
    right: 0;
    top: 148px;
  }
  .card--back .wordmark__name { font-size: 34px; }
  .card--back .wordmark__sub { font-size: 13px; margin-top: 10px; }
  .card--back .wordmark__mark { width: 24px; height: 24px; margin-bottom: 18px; }

  .site {
    position: absolute;
    left: 0;
    right: 0;
    bottom: 46px;
    text-align: center;
    font-size: 19px;
    letter-spacing: 0.03em;
  }
</style>
</head>
<body>

  <section class="card card--front" aria-label="Business card front">
    <div class="holder">
      <p class="holder__name">DANA WHITCOMBE</p>
      <p class="holder__role">FOUNDER</p>
    </div>

    <ul class="contact">
      <li class="contact__item">
        <svg class="contact__icon" viewBox="0 0 16 16" aria-hidden="true">
          <path d="M4 1.5l2.2 3-1.4 1.6c.8 1.8 2.2 3.3 4 4.2l1.6-1.4 3 2.2-1.2 2.6c-5.6-.4-10-4.8-10.4-10.4z" fill="none" stroke="var(--muted)" stroke-width="1.3" stroke-linejoin="round"/>
        </svg>
        <span>515.482.7093</span>
      </li>
      <li class="contact__item">
        <svg class="contact__icon" viewBox="0 0 16 16" aria-hidden="true">
          <rect x="1" y="3" width="14" height="10" fill="var(--muted)"/>
          <path d="M1 3l7 6 7-6M1 13l5-5M15 13l-5-5" fill="none" stroke="#fff" stroke-width="1.1"/>
        </svg>
        <span>info@htidesigns.com</span>
      </li>
      <li class="contact__item">
        <svg class="contact__icon" viewBox="0 0 16 16" aria-hidden="true">
          <g fill="none" stroke="var(--muted)" stroke-width="1.1">
            <circle cx="8" cy="8" r="6.5"/>
            <ellipse cx="8" cy="8" rx="3" ry="6.5"/>
            <path d="M1.5 8h13M2.5 4.8h11M2.5 11.2h11"/>
          </g>
        </svg>
        <span>www.htidesigns.com</span>
      </li>
    </ul>

    <div class="wordmark">
      <span class="wordmark__mark" aria-hidden="true"></span>
      <span class="wordmark__name">Hearth &amp; Tile</span>
      <span class="wordmark__sub">Interiors</span>
    </div>
  </section>

  <section class="card card--back" aria-label="Business card back">
    <div class="wordmark">
      <span class="wordmark__mark" aria-hidden="true"></span>
      <span class="wordmark__name">Hearth &amp; Tile</span>
      <span class="wordmark__sub">Interiors</span>
    </div>
    <p class="site">www.htidesigns.com</p>
  </section>

</body>
</html>
```